Project: Graphic Design Collateral for MVB Rising Stars Y2K Event
Client: Mauvelle Wellness Trust Rising Stars
Date: September 19, 2025
Time: 6:00 PM - 10:00 PM
Location: QLOFT, 4837 Pelorin Ave, 2nd Fl, Honolulu, HI 96814
Theme: Y2K
Objective:
To create visually engaging and on-brand graphic design collateral that effectively communicates the theme and excitement of the MVB Rising Stars Y2K Event.

Target Market(s)

Young professionals, ages 21-40, interested in supporting the Mauvelle Wellness Trust.

Industry/Entity Type

Healthcare

Requirements
Must have
• Collateral Requirements: • Invitation: o Digital and printable versions o Include event details (date, time, location, RSVP information) o Incorporate Y2K aesthetic (e.g., bold colors, chunky fonts, digital effects) Theming: Embrace the Y2K aesthetic with a focus on iconic technology of the era and gender-neutral visuals. Think shimmering ZIX chat boxes, witty away messages, and the iconic Pantry screen saver with the flying-over-green-hills-cow. Incorporate these elements into the design in a playful and inclusive way. For example, use a stylized chat box as a frame for event information or create social media graphics that mimic the look of early internet interfaces. This approach will not only evoke nostalgia but also add a unique and interactive dimension to the event's branding. Key takeaways: • Focus on iconic Y2K technology: ZIX chat boxes, away messages, Pantry screen saver. • Incorporate technology in a playful and inclusive way: Use as design elements, social media graphics. • Evoke nostalgia and add a unique dimension to the event's branding. • Typography: o Using the HEY! Here comes the big playlist look and feel. Utilize a mix of bold, chunky fonts reminiscent of early 2000s design (e.g., Impact, Arial Black) o Consider using a more modern font for readability and contrast.

```html
<!DOCTYPE html>
<html lang="en">
<head>
<meta charset="utf-8">
<title>MVB Rising Stars Y2K Event</title>
<link rel="stylesheet" href="https://fonts.googleapis.com/css2?family=Michroma&family=Syncopate:wght@700&family=Ultra&display=swap">
<style>
  :root {
    --ink: #111111;
    --bg-pink: #f0b4f0;
    --bg-violet: #b28cf5;
    --play-grey: #b4b0c6;
    --warn-top: #dff29a;
    --warn-bottom: #e9c79a;
    --bang: #d65cf0;
    --win-date: #b89ac8;
    --win-time: #b7e4f8;
    --win-location: #dde0dc;
    --panel-white: #f6f6f6;
    --loading: #f3df8c;
    --loading-sage: #b9c49a;
    --folder: #f1c7c4;
    --folder-line: #6a4a66;
    --cursor-line: #7a4a7a;
  }
  * { box-sizing: border-box; margin: 0; padding: 0; }
  html, body { width: 1200px; height: 1200px; overflow: hidden; }
  body { background: #ffffff; font-family: "Michroma", sans-serif; }

  .invite {
    position: relative; width: 1200px; height: 1200px; overflow: hidden;
    background:
      radial-gradient(circle at 22% 16%, rgba(255,255,255,.95) 0, rgba(255,255,255,0) 22%),
      radial-gradient(circle at 48% 40%, rgba(120,160,255,.8) 0, rgba(120,160,255,0) 30%),
      radial-gradient(circle at 85% 80%, rgba(175,215,255,.9) 0, rgba(175,215,255,0) 25%),
      radial-gradient(circle at 10% 60%, rgba(246,170,230,.9) 0, rgba(246,170,230,0) 35%),
      linear-gradient(160deg, var(--bg-pink) 0%, var(--bg-violet) 50%, var(--bg-pink) 100%);
  }

  .decor { position: absolute; inset: 0; width: 1200px; height: 1200px; }

  .event-title, .event-title-reflection {
    position: absolute; left: 0; width: 1200px; text-align: center;
    font-family: "Syncopate", "Arial Black", sans-serif; font-weight: 700; font-size: 40px;
    letter-spacing: 1px; color: var(--ink); line-height: 1; white-space: nowrap;
  }
  .event-title { top: 50px; }
  .event-title-reflection {
    top: 80px; transform: scaleY(-0.9); opacity: .45;
    -webkit-mask-image: linear-gradient(to top, #000 0%, transparent 90%);
    mask-image: linear-gradient(to top, #000 0%, transparent 90%);
  }

  .chat-window {
    position: absolute; border: 2px solid var(--ink); border-radius: 12px;
    display: flex; flex-direction: column; overflow: hidden;
  }
  .chat-bar { height: 52px; border-bottom: 2px solid var(--ink); display: flex; align-items: center; gap: 6px; padding: 0 18px; }
  .chat-bar.right { justify-content: flex-end; }
  .chat-dot { width: 17px; height: 17px; border: 2px solid var(--ink); border-radius: 50%; }
  .chat-body { flex: 1; display: flex; align-items: center; font-size: 21px; letter-spacing: 1px; color: var(--ink); white-space: nowrap; }
  .chat-foot { height: 26px; border-top: 2px solid var(--ink); }

  .window-date { left: 31px; top: 183px; width: 552px; height: 182px; background: var(--win-date); }
  .window-date .chat-body { justify-content: center; }
  .window-time { left: 719px; top: 288px; width: 449px; height: 205px; background: var(--win-time); }
  .window-time .chat-body { justify-content: flex-end; padding-right: 28px; }
  .window-location { left: 31px; top: 674px; width: 693px; height: 257px; background: var(--win-location); }
  .window-location .chat-body { padding-left: 16px; line-height: 1.3; }
  .location-lines { display: grid; grid-template-columns: auto auto; column-gap: 14px; }

  .headline-echo, .headline {
    position: absolute; left: 0; width: 1200px; text-align: center;
    font-family: "Ultra", "Cooper Black", serif; font-size: 88px; line-height: 1;
    transform: skewX(-10deg); white-space: nowrap;
  }
  .headline-echo { top: 568px; left: 30px; color: #f08ad8; opacity: .75; filter: blur(3px); }
  .headline { top: 552px; color: var(--ink); }

  .loading-label {
    position: absolute; left: 182px; top: 1080px;
    font-size: 22px; color: var(--loading); letter-spacing: 1px;
  }

  .partner-panel {
    position: absolute; left: 615px; top: 950px; width: 517px; height: 192px;
    background: var(--panel-white); border: 2px solid var(--ink); border-radius: 12px;
  }
  .partner-names {
    position: absolute; left: 0; top: 28px; width: 100%;
    text-align: center; font-family: "Michroma", sans-serif; font-size: 18px;
    line-height: 1.6; letter-spacing: 1px; color: var(--ink);
  }
  .rsvp-button {
    position: absolute; left: 153px; top: 123px; width: 210px; height: 50px;
    border: 2px solid var(--ink); border-radius: 10px; background: var(--panel-white);
    display: flex; align-items: center; justify-content: center;
    font-size: 24px; letter-spacing: 2px; color: var(--ink);
  }
</style>
</head>
<body>
<main class="invite">
  <svg class="decor" viewBox="0 0 1200 1200" aria-hidden="true">
    <defs>
      <linearGradient id="warnFill" x1="0" y1="0" x2="0" y2="1">
        <stop offset="0" stop-color="#dff29a"/>
        <stop offset="1" stop-color="#e9c79a"/>
      </linearGradient>
      <radialGradient id="playFill" cx=".5" cy=".5" r=".5">
        <stop offset="0" stop-color="#8f4fe0"/>
        <stop offset="1" stop-color="#c06ad8"/>
      </radialGradient>
    </defs>
    <circle cx="970" cy="213" r="207" fill="url(#playFill)" opacity=".9"/>
    <polygon points="872,114 1117,215 872,316" fill="#b4b0c6" opacity=".9"/>
    <path d="M585 318 Q600 300 615 318 L790 640 L410 640 Z" fill="url(#warnFill)" opacity=".9"/>
    <path d="M580 355 L620 355 L610 520 L590 520 Z" fill="#d65cf0"/>
    <rect x="585" y="545" width="30" height="38" fill="#d65cf0"/>
    <path d="M-40 1000 L60 1045 Q80 1055 100 1050 L140 1040 Q160 1040 165 1060 L180 1210 L-40 1210 Z"
          fill="#f1c7c4" stroke="#6a4a66" stroke-width="8"/>
    <path d="M-40 1090 L130 1100 Q150 1102 145 1125 L120 1210 L-40 1210 Z"
          fill="#f3e7a8" stroke="#6a4a66" stroke-width="8"/>
    <rect x="182" y="1110" width="195" height="40" rx="6" fill="#f3df8c"/>
    <rect x="393" y="1110" width="25" height="40" rx="4" fill="#f3df8c"/>
    <rect x="435" y="1110" width="25" height="40" rx="4" fill="#b9c49a"/>
    <rect x="477" y="1110" width="25" height="40" rx="4" fill="#f3df8c"/>
    <rect x="519" y="1110" width="25" height="40" rx="4" fill="#f3df8c"/>
    <rect x="561" y="1110" width="25" height="40" rx="4" fill="#b9c49a"/>
  </svg>

  <h1 class="event-title">MVB RISING STARS Y2K EVENT</h1>
  <div class="event-title-reflection" aria-hidden="true">MVB RISING STARS Y2K EVENT</div>

  <section class="chat-window window-date">
    <div class="chat-bar right"><span class="chat-dot"></span><span class="chat-dot"></span><span class="chat-dot"></span></div>
    <p class="chat-body">DATE: SEPTEMBER 19, 2025</p>
    <div class="chat-foot"></div>
  </section>

  <section class="chat-window window-time">
    <div class="chat-bar right"><span class="chat-dot"></span><span class="chat-dot"></span><span class="chat-dot"></span></div>
    <p class="chat-body">TIME: 6:00 PM - 10:00 PM</p>
    <div class="chat-foot"></div>
  </section>

  <div class="headline-echo" aria-hidden="true">USING THE NOW!</div>
  <h2 class="headline">USING THE NOW!</h2>

  <section class="chat-window window-location">
    <div class="chat-bar"><span class="chat-dot"></span><span class="chat-dot"></span><span class="chat-dot"></span></div>
    <div class="chat-body">
      <div class="location-lines">
        <span>LOCATION:</span><span>QLOFT, 4837 PELORIN AVE,</span>
        <span></span><span>2ND FL, HONOLULU, HI 96814</span>
      </div>
    </div>
    <div class="chat-foot"></div>
  </section>

  <p class="loading-label">LOADING...</p>

  <section class="partner-panel">
    <div class="partner-names">
      <p>KALEO COASTAL CARE</p>
      <p>MAUVELLE WELLNESS TRUST</p>
    </div>
    <div class="rsvp-button">YES</div>
  </section>

  <svg class="decor" viewBox="0 0 1200 1200" aria-hidden="true">
    <path d="M945 1100 L1070 1190 L1020 1195 L1050 1240 L1020 1250 L995 1205 L960 1230 Z"
          fill="#ffffff" stroke="#7a4a7a" stroke-width="5" stroke-dasharray="8 4"/>
  </svg>
</main>
</body>
</html>
```